Billboard design - consider what a billboard is

Design a billboard using my logo - Billboard is 6m x 3m
A Billboard is advertising for my company that is on a big sign.

Has to be clean and easy to read, and ideally highlights that we are Residential and Commercial builders.

Keep it clean and easy to read

The contact number for the board is

022 583 7092
www.harbourframeworks.co.nz
info@harbourframeworks.co.nz

Doesnt have to have all contact details if it doesnt fit

Has to catch peoples attention to contact us if they need a builder

Can you please change the sign to be all white writing, with black background ?
Updates

Please consider what a billboard is...

The design needs to be suitable for a billboard..

Target Market(s)

people driving past

Industry/Entity Type

Construction

Logo Text

Wellington Builder, website email address, contact number

Colors
0054AA
0677BA
7BADD7
CADEEF
E8F1F8

Requirements
Must have
• Easy to read
Nice to have
• easy to read, can clearly see contact details

```html
<!DOCTYPE html>
<html lang="en">
<head>
<meta charset="utf-8">
<title>Harbour Frameworks – Billboard 6m x 3m</title>
<link rel="stylesheet" href="https://fonts.googleapis.com/css2?family=Barlow:wght@400;600;700&family=Barlow+Semi+Condensed:wght@700&display=swap">
<style>
  :root {
    --stage: #58585a;
    --board: #ffffff;
    --brand-blue: #5a8ac8;
    --warm-grey: #6d6567;
    --label: #ffffff;
  }
  html, body {
    margin: 0;
    padding: 0;
    width: 1200px;
    height: 1000px;
    overflow: hidden;
    background: var(--stage);
  }
  .canvas {
    position: relative;
    width: 1200px;
    height: 1000px;
    font-family: "Barlow", Arial, sans-serif;
  }
  .size-label {
    position: absolute;
    left: 193px;
    top: 236px;
    margin: 0;
    font-weight: 400;
    font-size: 36px;
    color: var(--label);
    letter-spacing: 0.5px;
  }
  .billboard {
    position: absolute;
    left: 189px;
    top: 294px;
    width: 822px;
    height: 411px;
    background: var(--board);
    box-shadow: 6px 6px 6px rgba(0,0,0,0.35);
    overflow: hidden;
  }
  .brand-name {
    position: absolute;
    left: 60px;
    top: 96px;
    margin: 0;
    color: var(--brand-blue);
    font-weight: 700;
    line-height: 1;
  }
  .brand-name .primary {
    display: block;
    font-size: 104px;
    letter-spacing: -1px;
  }
  .brand-name .secondary {
    display: block;
    font-size: 44px;
    letter-spacing: 3px;
    margin-top: 4px;
    text-transform: uppercase;
  }
  .divider {
    position: absolute;
    left: 490px;
    top: 137px;
    width: 1.5px;
    height: 84px;
    background: var(--warm-grey);
  }
  .tagline {
    position: absolute;
    left: 509px;
    top: 135px;
    margin: 0;
    font-weight: 600;
    font-size: 26px;
    line-height: 31px;
    color: var(--warm-grey);
    text-transform: uppercase;
    letter-spacing: 0.3px;
  }
  .contact-band {
    position: absolute;
    left: 0;
    top: 0;
    width: 822px;
    height: 411px;
  }
  .phone-number {
    position: absolute;
    left: 111px;
    top: 321px;
    height: 70px;
    line-height: 70px;
    margin: 0;
    font-family: "Barlow Semi Condensed", "Barlow", Arial, sans-serif;
    font-weight: 700;
    font-size: 62px;
    color: #ffffff;
    letter-spacing: 0.5px;
  }
</style>
</head>
<body>
<div class="canvas">
  <p class="size-label">Size: 6m x 3m</p>

  <section class="billboard" aria-label="Harbour Frameworks billboard">
    <svg class="contact-band" viewBox="0 0 822 411" aria-hidden="true">
      <polygon points="0,321 552,321 484,391 0,391" fill="var(--brand-blue)"/>
      <rect x="497" y="365" width="325" height="14" fill="var(--warm-grey)"/>
      <g class="phone-icon" fill="#ffffff" transform="translate(57,339)">
        <path d="M6 2 C9 0 12 1 13 4 L16 12 C17 14 16 16 14 17 L11 19 C13 25 17 29 22 31 L24 28 C25 26 27 25 29 26 L36 29 C39 30 40 33 38 36 L35 39 C33 41 29 41 26 40 C14 36 5 27 1 15 C0 11 1 7 3 5 Z"/>
        <path d="M21 10 A9 9 0 0 1 30 19" fill="none" stroke="#ffffff" stroke-width="2.4" stroke-linecap="round"/>
        <path d="M22 4 A15 15 0 0 1 36 18" fill="none" stroke="#ffffff" stroke-width="2.4" stroke-linecap="round"/>
        <path d="M21 16 A3 3 0 0 1 24 19" fill="none" stroke="#ffffff" stroke-width="2.4" stroke-linecap="round"/>
      </g>
    </svg>

    <h1 class="brand-name">
      <span class="primary">Harbour</span>
      <span class="secondary">Frameworks</span>
    </h1>

    <div class="divider"></div>
    <p class="tagline">We are residential<br>and commercial<br>builders.</p>

    <p class="phone-number">022 583 7092</p>
  </section>
</div>
</body>
</html>
```